Freeze Dried Candy Pouch Design - Australia

Tundra Pop is an online Australian Freeze Dried Candy company that is looking for a pouch design for our Freeze Dried Candy.

We would like one pouch design for all of our products, so more generic in that sense but perhaps a section at the bottom of the front of the page where we can put a small label for each product to tell what it is.

We would like it to fun, colorful but keep behind our logo white as that fits with our current styling. Happy to have a window as well or not, up to you but window would create interest. I've uploaded our logo source and some designs we saw online for some reference but doesn't have to match or be similar.

We'd like this to cover the back;

Fair Dinkum Candy Blastoff with Freeze-Dried Treats!

Get ready for a ripper taste sensation! Our freeze-dried lollies take your favourites to a whole new level. Here's what makes them the bee's knees:

Intensified Flavour: The freeze-drying process sucks out the moisture, concentrating the candy's deliciousness for an explosion of flavour in every bite!

Light & Crispy: No more chewy or sticky stuff here! Freeze-dried treats turn into delightful, light, and airy puffs with a satisfying crunch.

Perfect for Snacking & Heaps More: Enjoy them straight from the pouch for a unique sweet treat, or chuck 'em on yoghurt, ice cream, or even your favourite cocktail for a bit of fun, crunchy texture!

Long-lasting Adventure: Because there's no moisture, freeze-dried candy has a longer shelf life than regular lollies, making them perfect for chucking in lunchboxes or taking on your outdoor adventures.

So buckle up and experience candy like never before!

Socials
Share the Joy
Tag us in your snack adventures on social media with #FreezeDriedCandy for a chance to be featured!

Possibly list where to find us via socials handle which is tundrapop.au for facebook, tiktok and instagram

Our website address is www.tundrapop.com.au and we'd like to have a spot we can put a QR code to go to nutritional information instead of having it listed on the back as we don't need this right now.

The pouch will be used for printing in the future.

```html
<!DOCTYPE html>
<html lang="en">
<head>
<meta charset="utf-8">
<title>Tundra Pop – Freeze Dried Candy Pouches</title>
<link rel="stylesheet" href="https://fonts.googleapis.com/css2?family=Courgette&family=Fredoka:wght@500&display=swap">
<style>
  :root {
    --backdrop: #e3e3e3;
    --pouch-white: #f4f4f4;
    --pouch-edge: #d6d6d6;
    --zip-grey: #d2d2d2;
    --gold-light: #f2c14e;
    --gold-deep: #e59412;
    --teal: #0f8f8f;
    --lime: #b9cf2c;
    --plum-dot: #8a2a7a;
    --grape-light: #5a3a8e;
    --grape-deep: #12175e;
    --berry-light: #c9439a;
    --berry-deep: #8e0c5a;
    --brand-pink: #e0287a;
    --badge-pink: #e8337f;
    --label-text: #ffffff;
  }
  * { margin: 0; padding: 0; box-sizing: border-box; }
  html, body { width: 1200px; height: 775px; overflow: hidden; }
  body { background: var(--backdrop); position: relative; }
  .pouch { position: absolute; top: 78px; width: 415px; height: 636px; }
  .pouch--grape { left: 93px; }
  .pouch--raspberry { left: 693px; }
  .pouch svg { display: block; width: 100%; height: 100%; }
  .brand-name {
    font-family: "Courgette", cursive;
    font-size: 56px;
    fill: var(--brand-pink);
  }
  .product-name {
    font-family: "Courgette", cursive;
    fill: var(--label-text);
  }
  .product-name--grape { font-size: 27px; }
  .product-name--raspberry { font-size: 30px; }
  .badge-value {
    font-family: "Fredoka", sans-serif;
    font-weight: 500;
    font-size: 12px;
    fill: var(--badge-pink);
  }
  .badge-unit {
    font-family: "Fredoka", sans-serif;
    font-weight: 500;
    font-size: 7px;
    fill: var(--badge-pink);
  }
</style>
</head>
<body>

<div class="pouch pouch--grape">
  <svg viewBox="0 0 415 636" role="img" aria-label="Tundra Pop pouch, Grapeberry Puffs – Crunchee Munchez, 20 pieces">
    <defs>
      <linearGradient id="gold-a" x1="0" y1="0" x2="1" y2="0">
        <stop offset="0" stop-color="var(--gold-light)"/>
        <stop offset="1" stop-color="var(--gold-deep)"/>
      </linearGradient>
      <linearGradient id="label-a" x1="0" y1="0" x2="1" y2="0">
        <stop offset="0" stop-color="var(--grape-light)"/>
        <stop offset="1" stop-color="var(--grape-deep)"/>
      </linearGradient>
      <clipPath id="body-a"><rect x="0" y="0" width="415" height="636" rx="14"/></clipPath>
    </defs>
    <rect x="0" y="0" width="415" height="636" rx="14" fill="var(--pouch-white)" stroke="var(--pouch-edge)"/>
    <g clip-path="url(#body-a)">
      <path class="teal-wave" fill="var(--teal)" d="M300 170 C330 145 372 150 415 168 V312 C382 298 352 304 328 316 C318 262 310 212 300 170 Z"/>
      <path class="gold-sweep" fill="url(#gold-a)" d="M0 0 H365 C358 62 330 98 262 98 C175 98 115 160 108 250 C103 320 130 360 175 378 C120 378 60 340 20 285 L0 285 Z"/>
      <rect class="zip-corner" x="365" y="0" width="50" height="88" fill="var(--zip-grey)"/>
      <line x1="0" y1="88" x2="415" y2="88" stroke="#ffffff" stroke-opacity=".5" stroke-width="2"/>
      <path class="lime-blob" fill="var(--lime)" d="M0 370 C60 380 90 440 85 500 C80 550 50 585 15 596 L0 596 Z"/>
      <path class="product-label" fill="url(#label-a)" d="M145 490 C140 430 220 405 305 402 C360 400 395 408 415 418 V636 H300 C260 600 200 570 160 555 C140 540 142 520 145 490 Z"/>
    </g>
    <rect class="hang-slot" x="162" y="23" width="87" height="23" rx="9" fill="#ffffff"/>
    <circle cx="387" cy="347" r="10" fill="var(--plum-dot)"/>
    <circle cx="112" cy="418" r="16" fill="var(--lime)"/>
    <circle cx="76" cy="597" r="10" fill="var(--plum-dot)"/>
    <text class="brand-name" x="214" y="285" text-anchor="middle">Tundra Pop</text>
    <text class="product-name product-name--grape" transform="translate(268 487) rotate(-14)" text-anchor="middle">
      <tspan x="-4" y="-10">Grapeberry Puffs –</tspan>
      <tspan x="8" y="26">Crunchee Munchez</tspan>
    </text>
    <g class="pack-badge">
      <circle cx="102" cy="551" r="24" fill="#ffffff" stroke="var(--badge-pink)" stroke-width="1.5"/>
      <circle cx="102" cy="551" r="19" fill="none" stroke="var(--badge-pink)" stroke-width=".8" stroke-dasharray="1.5 1.5"/>
      <text class="badge-value" x="102" y="553" text-anchor="middle">20</text>
      <text class="badge-unit" x="102" y="561" text-anchor="middle">pc</text>
    </g>
  </svg>
</div>

<div class="pouch pouch--raspberry">
  <svg viewBox="0 0 415 636" role="img" aria-label="Tundra Pop pouch, Raspberry Blocks–Bloop, 100 grams">
    <defs>
      <linearGradient id="gold-b" x1="0" y1="0" x2="1" y2="0">
        <stop offset="0" stop-color="var(--gold-light)"/>
        <stop offset="1" stop-color="var(--gold-deep)"/>
      </linearGradient>
      <linearGradient id="label-b" x1="0" y1="0" x2="1" y2="0">
        <stop offset="0" stop-color="var(--berry-light)"/>
        <stop offset="1" stop-color="var(--berry-deep)"/>
      </linearGradient>
      <clipPath id="body-b"><rect x="0" y="0" width="415" height="636" rx="14"/></clipPath>
    </defs>
    <rect x="0" y="0" width="415" height="636" rx="14" fill="var(--pouch-white)" stroke="var(--pouch-edge)"/>
    <g clip-path="url(#body-b)">
      <path class="teal-wave" fill="var(--teal)" d="M300 170 C330 145 372 150 415 168 V312 C382 298 352 304 328 316 C318 262 310 212 300 170 Z"/>
      <path class="gold-sweep" fill="url(#gold-b)" d="M0 0 H365 C358 62 330 98 262 98 C175 98 115 160 108 250 C103 320 130 360 175 378 C120 378 60 340 20 285 L0 285 Z"/>
      <rect class="zip-corner" x="365" y="0" width="50" height="88" fill="var(--zip-grey)"/>
      <line x1="0" y1="88" x2="415" y2="88" stroke="#ffffff" stroke-opacity=".5" stroke-width="2"/>
      <path class="lime-blob" fill="var(--lime)" d="M0 370 C60 380 90 440 85 500 C80 550 50 585 15 596 L0 596 Z"/>
      <path class="product-label" fill="url(#label-b)" d="M145 490 C140 430 220 405 305 402 C360 400 395 408 415 418 V636 H300 C260 600 200 570 160 555 C140 540 142 520 145 490 Z"/>
    </g>
    <rect class="hang-slot" x="162" y="23" width="87" height="23" rx="9" fill="#ffffff"/>
    <circle cx="387" cy="347" r="10" fill="var(--plum-dot)"/>
    <circle cx="112" cy="418" r="16" fill="var(--lime)"/>
    <circle cx="76" cy="597" r="10" fill="var(--plum-dot)"/>
    <text class="brand-name" x="214" y="285" text-anchor="middle">Tundra Pop</text>
    <text class="product-name product-name--raspberry" transform="translate(258 483) rotate(-9)" text-anchor="middle">
      <tspan x="0" y="-10">Raspberry</tspan>
      <tspan x="4" y="28">Blocks–Bloop</tspan>
    </text>
    <g class="pack-badge">
      <circle cx="102" cy="551" r="24" fill="#ffffff" stroke="var(--badge-pink)" stroke-width="1.5"/>
      <circle cx="102" cy="551" r="19" fill="none" stroke="var(--badge-pink)" stroke-width=".8" stroke-dasharray="1.5 1.5"/>
      <text class="badge-value" x="102" y="553" text-anchor="middle">100</text>
      <text class="badge-unit" x="102" y="561" text-anchor="middle">gr</text>
    </g>
  </svg>
</div>

</body>
</html>
```